Indian Takeaway Menu -

I would like to have double parallel fold A4 sheet menu.
A4 sheet cut in half and attached to the other half to make the sheet 4 small pages long.

Colors
abd036
ffffff

Requirements
Must have
• Please check new attachments - menu size and layout is not correct.
• I would like to add Dark brown colour. A4 sheet folded 4x Menu layout pocket size.
Nice to have
• Dark Brown - Parrot Green and very light Brown

```html
<!DOCTYPE html>
<html lang="en">
<head>
<meta charset="utf-8">
<title>Saffron Hearth – Menu Cover</title>
<link rel="stylesheet" href="https://fonts.googleapis.com/css2?family=Arimo:wght@400;700&display=swap">
<style>
  :root {
    --paper: #ffffff;
    --parrot-green: #d3e05a;
    --parrot-green-soft: #e6eda2;
    --dark-brown: #2e1d16;
    --text-dark: #231a14;
    --accent-red: #d9342b;
  }
  * { box-sizing: border-box; margin: 0; padding: 0; }
  html, body {
    width: 1200px;
    height: 848px;
    overflow: hidden;
    background: var(--paper);
  }
  .canvas {
    position: relative;
    width: 1200px;
    height: 848px;
    background: var(--paper);
    font-family: "Arimo", Arial, sans-serif;
    color: var(--text-dark);
  }
  .cover-panel {
    position: absolute;
    left: 309px;
    top: 80px;
    width: 573px;
    height: 749px;
    background: linear-gradient(
      to bottom,
      var(--paper) 0%,
      var(--parrot-green-soft) 10%,
      var(--parrot-green) 22%,
      var(--parrot-green) 80%,
      var(--parrot-green-soft) 93%,
      #f2f5d8 100%
    );
  }
  .brand {
    position: absolute;
    left: 0;
    right: 0;
    top: 378px;
    text-align: center;
  }
  .brand-name {
    font-size: 38px;
    font-weight: 700;
    color: var(--dark-brown);
    letter-spacing: 0.5px;
    line-height: 1;
  }
  .brand-rule {
    display: block;
    width: 330px;
    height: 3px;
    margin: 60px auto 0;
    background: var(--dark-brown);
    border-radius: 2px;
  }
  .tagline {
    margin-top: 14px;
    font-size: 19px;
    font-weight: 400;
    letter-spacing: 0.2px;
    color: var(--text-dark);
  }
  .contact-row {
    position: absolute;
    top: 694px;
    left: 0;
    right: 0;
    font-size: 16px;
    line-height: 18px;
  }
  .contact-item {
    position: absolute;
    display: flex;
    align-items: center;
    gap: 8px;
    white-space: nowrap;
  }
  .contact-web { left: 69px; }
  .contact-phone { left: 316px; }
  .contact-icon { width: 18px; height: 18px; flex: none; }
</style>
</head>
<body>
  <main class="canvas">
    <section class="cover-panel">
      <header class="brand">
        <h1 class="brand-name">Saffron Hearth</h1>
        <span class="brand-rule"></span>
        <p class="tagline">AUTHENTIC INDIAN FOOD AT HOME</p>
      </header>

      <footer class="contact-row">
        <div class="contact-item contact-web">
          <svg class="contact-icon" viewBox="0 0 18 18" aria-hidden="true">
            <circle cx="9" cy="9" r="8" fill="var(--accent-red)"/>
            <g fill="none" stroke="#ffffff" stroke-width="1">
              <circle cx="9" cy="9" r="6"/>
              <ellipse cx="9" cy="9" rx="2.6" ry="6"/>
              <line x1="3" y1="9" x2="15" y2="9"/>
              <line x1="4" y1="6" x2="14" y2="6"/>
              <line x1="4" y1="12" x2="14" y2="12"/>
            </g>
          </svg>
          <span>www.saffronhearth.ie</span>
        </div>
        <div class="contact-item contact-phone">
          <svg class="contact-icon" viewBox="0 0 18 18" aria-hidden="true">
            <rect x="1" y="2" width="16" height="14" rx="2" fill="var(--accent-red)"/>
            <rect x="3" y="4" width="4" height="10" rx="1" fill="#ffffff"/>
            <rect x="9" y="4" width="6" height="3" fill="#ffffff"/>
            <g fill="#ffffff">
              <rect x="9" y="9" width="1.6" height="1.6"/>
              <rect x="11.2" y="9" width="1.6" height="1.6"/>
              <rect x="13.4" y="9" width="1.6" height="1.6"/>
              <rect x="9" y="11.6" width="1.6" height="1.6"/>
              <rect x="11.2" y="11.6" width="1.6" height="1.6"/>
              <rect x="13.4" y="11.6" width="1.6" height="1.6"/>
            </g>
          </svg>
          <span>015550184, 015550186</span>
        </div>
      </footer>
    </section>
  </main>
</body>
</html>
```